Norvel Hand Wash

Design hand washes. Total 12 variants to be designed.

Variants name are:

1) MILK &OLIVE
2) Shea Butter
3) Hidden Dawn
4) Cream and Peach
5) Milk and Honey
6) Amber Whisper
7) Bakhour
8) Musk
9) White Oud
10) Black Oud
11) Rose Oud
12) Oud & Sandalwood

Labels can be on transparent sticker or background colors. All variants will be differentiated by fragrances and color. Bottle will be transparent. Pumps used for dispensing will be in Black or Transparent Color.

Designers can initially present designs of 4-5 variants initially. Later based on feedback, they can work out on more.

Bottle is 400ml and shape is rectangle. Ignore the size on bottle picture. Bottle keyline is attached.

Target Market(s)

B+, B, C+

Requirements
Must have
• Some relation to the variant names

```html
<!DOCTYPE html>
<html lang="en">
<head>
<meta charset="utf-8">
<title>Norvel Hand Wash Labels</title>
<link rel="stylesheet" href="https://fonts.googleapis.com/css2?family=Della+Respira&display=swap">
<style>
  :root {
    --page: #ffffff;
    --brand: #5b4a8f;
    --olive-ring: #0f9a82;
    --olive-type: #8cbf4a;
    --olive-wave-a: #3aa7b8;
    --olive-wave-b: #9ccc5a;
    --peach-ring: #f0926a;
    --peach-type: #f0944e;
    --peach-wave-a: #f5a878;
    --peach-wave-b: #f8c79a;
    --honey-ring: #f2cf52;
    --honey-type: #f2a33a;
    --honey-wave-a: #f6b552;
    --honey-wave-b: #f9dc8a;
    --amber-ring: #f1e277;
    --amber-type: #e4b57e;
    --amber-wave-a: #eec69c;
    --amber-wave-b: #f5eaa0;
    --rose-ring: #ef9a82;
    --rose-type: #e0735a;
    --rose-wave-a: #ec8c78;
    --rose-wave-b: #f6c2a8;
  }
  * { margin: 0; padding: 0; box-sizing: border-box; }
  html, body { width: 1200px; height: 1200px; overflow: hidden; background: var(--page); }
  body { position: relative; font-family: "Della Respira", Georgia, serif; }

  .label {
    position: absolute;
    width: 318px;
    height: 565px;
    border-radius: 10px;
    overflow: hidden;
  }
  .label--olive { left: 107px; top: 25px;  --ring: var(--olive-ring); --type: var(--olive-type); --wa: var(--olive-wave-a); --wb: var(--olive-wave-b); }
  .label--peach { left: 439px; top: 25px;  --ring: var(--peach-ring); --type: var(--peach-type); --wa: var(--peach-wave-a); --wb: var(--peach-wave-b); }
  .label--honey { left: 773px; top: 25px;  --ring: var(--honey-ring); --type: var(--honey-type); --wa: var(--honey-wave-a); --wb: var(--honey-wave-b); }
  .label--amber { left: 107px; top: 618px; --ring: var(--amber-ring); --type: var(--amber-type); --wa: var(--amber-wave-a); --wb: var(--amber-wave-b); }
  .label--rose  { left: 439px; top: 618px; --ring: var(--rose-ring);  --type: var(--rose-type);  --wa: var(--rose-wave-a);  --wb: var(--rose-wave-b); }

  .label__pattern {
    position: absolute;
    inset: 0;
    background: linear-gradient(160deg, var(--wa) 0%, var(--wb) 50%, var(--wa) 100%);
    opacity: 0.55;
  }

  .label__brand {
    position: absolute;
    top: 52px;
    left: 0;
    right: 0;
    display: flex;
    justify-content: center;
  }
  .brand-mark {
    background: var(--page);
    border-radius: 8px;
    padding: 4px 14px 6px;
    font-size: 34px;
    line-height: 1;
    color: var(--brand);
    display: flex;
    flex-direction: column;
    align-items: center;
  }
  .brand-mark__tagline {
    font-size: 7px;
    color: var(--brand);
    align-self: flex-end;
    margin-top: 1px;
  }

  .label__oval {
    position: absolute;
    left: 28px;
    top: 146px;
    width: 262px;
    height: 308px;
    border-radius: 50%;
    border: 3px solid var(--ring);
    background: radial-gradient(ellipse at center, #fff 72%, rgba(255,255,255,0.85) 100%);
    display: flex;
    flex-direction: column;
    align-items: center;
    justify-content: center;
    text-align: center;
  }
  .oval__dot {
    position: absolute;
    left: 50%;
    width: 7px;
    height: 7px;
    margin-left: -3.5px;
    border-radius: 50%;
    background: var(--ring);
  }
  .oval__dot--top { top: 51px; }
  .oval__dot--bottom { bottom: 44px; }

  .variant-name {
    color: var(--type);
    font-size: 52px;
    line-height: 0.98;
    letter-spacing: -1px;
    font-weight: 400;
  }
  .variant-name--long { font-size: 46px; letter-spacing: 0; }
  .product-type {
    color: var(--type);
    font-size: 16px;
    margin-top: 10px;
    letter-spacing: -0.3px;
  }

  .label__volume {
    position: absolute;
    left: 0;
    right: 0;
    bottom: 12px;
    text-align: center;
    font-size: 14px;
    color: var(--brand);
  }
</style>
</head>
<body>

  <section class="label label--olive">
    <div class="label__pattern" role="img" aria-label="Wavy line pattern in teal and green"></div>
    <div class="label__brand"><div class="brand-mark">Norvel<span class="brand-mark__tagline">Air Freshener</span></div></div>
    <div class="label__oval">
      <span class="oval__dot oval__dot--top"></span>
      <h2 class="variant-name">MILK&amp;<br>OLIVE</h2>
      <p class="product-type">HAND WASH</p>
      <span class="oval__dot oval__dot--bottom"></span>
    </div>
    <p class="label__volume">400ML</p>
  </section>

  <section class="label label--peach">
    <div class="label__pattern" role="img" aria-label="Wavy line pattern in peach and orange"></div>
    <div class="label__brand"><div class="brand-mark">Norvel<span class="brand-mark__tagline">Air Freshener</span></div></div>
    <div class="label__oval">
      <span class="oval__dot oval__dot--top"></span>
      <h2 class="variant-name">CREAM&amp;<br>PEACH</h2>
      <p class="product-type">HAND WASH</p>
      <span class="oval__dot oval__dot--bottom"></span>
    </div>
    <p class="label__volume">400ML</p>
  </section>

  <section class="label label--honey">
    <div class="label__pattern" role="img" aria-label="Wavy line pattern in honey yellow and orange"></div>
    <div class="label__brand"><div class="brand-mark">Norvel<span class="brand-mark__tagline">Air Freshener</span></div></div>
    <div class="label__oval">
      <span class="oval__dot oval__dot--top"></span>
      <h2 class="variant-name">MILK&amp;<br>HONEY</h2>
      <p class="product-type">HAND WASH</p>
      <span class="oval__dot oval__dot--bottom"></span>
    </div>
    <p class="label__volume">400ML</p>
  </section>

  <section class="label label--amber">
    <div class="label__pattern" role="img" aria-label="Wavy line pattern in soft amber and pale yellow"></div>
    <div class="label__brand"><div class="brand-mark">Norvel<span class="brand-mark__tagline">Air Freshener</span></div></div>
    <div class="label__oval">
      <span class="oval__dot oval__dot--top"></span>
      <h2 class="variant-name variant-name--long">AMBER<br>WHISPER</h2>
      <p class="product-type">HAND WASH</p>
      <span class="oval__dot oval__dot--bottom"></span>
    </div>
    <p class="label__volume">400ML</p>
  </section>

  <section class="label label--rose">
    <div class="label__pattern" role="img" aria-label="Wavy line pattern in rose and coral"></div>
    <div class="label__brand"><div class="brand-mark">Norvel<span class="brand-mark__tagline">Air Freshener</span></div></div>
    <div class="label__oval">
      <span class="oval__dot oval__dot--top"></span>
      <h2 class="variant-name" style="font-size:60px">ROSE<br>OUD</h2>
      <p class="product-type">HAND WASH</p>
      <span class="oval__dot oval__dot--bottom"></span>
    </div>
    <p class="label__volume">400ML</p>
  </section>

</body>
</html>
```